Dunmore Plumbing LLC business card

Would like a modern looking business card with my new logo

Contact Information for Business Card

Calvin Dunmore 2418 Elm Hollow Rd Larkhaven 06999, Dunmoreplumbingllc@exampletrade.com, 203-555-0174

```html
<!DOCTYPE html>
<html lang="en">
<head>
<meta charset="utf-8">
<title>Dunmore Plumbing LLC – Business Card</title>
<link rel="stylesheet" href="https://fonts.googleapis.com/css2?family=Arimo:wght@400;700&display=swap">
<style>
  :root {
    --page-bg: #c9c9c9;
    --brand-blue: #04a9e8;
    --card-white: #ffffff;
    --ink: #1a1a1a;
    --muted-text: #333333;
    --faint-decor: #ececec;
    --faint-decor-blue: #0697d0;
  }
  * { box-sizing: border-box; margin: 0; padding: 0; }
  html, body { width: 1200px; height: 900px; overflow: hidden; }
  body {
    background: var(--page-bg);
    font-family: "Arimo", Arial, sans-serif;
    position: relative;
  }
  .card {
    position: absolute;
    left: 320px;
    width: 560px;
    height: 320px;
    border-radius: 30px;
    overflow: hidden;
    box-shadow: 0 6px 18px rgba(0,0,0,0.25);
  }
  .card--front { top: 100px; background: var(--brand-blue); }
  .card--back { top: 480px; background: var(--card-white); }

  .decor-band {
    position: absolute;
    right: 0;
    top: 40px;
    width: 200px;
    height: 150px;
    border-radius: 24px 0 0 24px;
  }
  .card--front .decor-band { background: linear-gradient(90deg, rgba(6,151,208,0) 0%, var(--faint-decor-blue) 45%); }
  .card--back .decor-band { background: linear-gradient(90deg, rgba(236,236,236,0) 0%, var(--faint-decor) 45%); }

  .wordmark {
    position: absolute;
    display: flex;
    align-items: center;
    gap: 12px;
    font-weight: 700;
    font-size: 34px;
    letter-spacing: 1px;
    text-transform: uppercase;
    line-height: 1;
    white-space: nowrap;
  }
  .wordmark__mark { width: 26px; height: 26px; flex: none; }
  .card--front .wordmark { left: 50%; top: 50%; transform: translate(-50%, -50%); color: var(--card-white); }
  .card--front .wordmark__mark { background: var(--card-white); }
  .card--back .wordmark { left: 40px; top: 60px; color: var(--ink); font-size: 30px; }
  .card--back .wordmark__mark { background: var(--brand-blue); }

  .holder-name {
    position: absolute;
    left: 44px;
    top: 150px;
    color: var(--brand-blue);
    font-weight: 700;
    font-size: 24px;
    text-transform: uppercase;
    letter-spacing: 0.5px;
  }
  .contact-list {
    position: absolute;
    left: 44px;
    bottom: 36px;
    list-style: none;
    color: var(--muted-text);
    font-size: 15px;
    line-height: 1.5;
  }
  .contact-list li { display: flex; align-items: center; gap: 8px; }
  .contact-list svg { width: 15px; height: 15px; flex: none; }
  .address {
    position: absolute;
    right: 36px;
    bottom: 82px;
    text-align: right;
    color: var(--muted-text);
    font-size: 15px;
    line-height: 1.35;
    font-style: normal;
  }
</style>
</head>
<body>
  <section class="card card--front" aria-label="Card front">
    <div class="decor-band" role="img" aria-label="Faint faucet graphic"></div>
    <div class="wordmark"><span class="wordmark__mark"></span>Dunmore Plumbing LLC</div>
  </section>

  <section class="card card--back" aria-label="Card back">
    <div class="decor-band" role="img" aria-label="Faint faucet graphic"></div>
    <div class="wordmark"><span class="wordmark__mark"></span>Dunmore Plumbing LLC</div>
    <h1 class="holder-name">Calvin Dunmore</h1>
    <ul class="contact-list">
      <li>
        <svg viewBox="0 0 24 24" aria-hidden="true"><path fill="#04a9e8" d="M6.6 10.8a15.1 15.1 0 0 0 6.6 6.6l2.2-2.2a1 1 0 0 1 1-.25 11.4 11.4 0 0 0 3.6.57 1 1 0 0 1 1 1V20a1 1 0 0 1-1 1A17 17 0 0 1 3 4a1 1 0 0 1 1-1h3.5a1 1 0 0 1 1 1c0 1.25.2 2.45.57 3.6a1 1 0 0 1-.25 1z"/></svg>
        203-555-0174
      </li>
      <li>
        <svg viewBox="0 0 24 24" aria-hidden="true"><path fill="#04a9e8" d="M2 5h20v14H2z"/><path fill="none" stroke="#fff" stroke-width="1.8" d="M2 5l10 8 10-8"/></svg>
        Dunmoreplumbingllc@exampletrade.com
      </li>
    </ul>
    <address class="address">2418 Elm Hollow Rd<br>Larkhaven 06999</address>
  </section>
</body>
</html>
```